Rising Paths Web Design

I am starting a new company that will provide LIFE COACHING services - I have tried to design a website, but it's too complicated. Right now, it's just me - I'm the only person that will provide services through the website - I have used artmarket to purchase a logo (see below). I want to be able to update the website myself, but need a template - basic design. Because I am not technologically savvy enough to explain in words - I basically want to have a website that will provide basic information about my services (coaching), a page about me and my background, hopefully scheduling possibilities, and testimonials — also a page for writing/blogs. I bought a website through NetHarbor - so when I have a template, I guess I”d use that - but maybe I’ll need to work with a designer to actually get it up on the internet. I have a head shot that I’ll upload, too.
Target Market(s)
Clients from the independent (private school) world - teachers, administrators
Number of Pages Required
4 page
Look and feel
Each slider illustrates characteristics of the customer's brand and the style your logo design should communicate.

```html
<!DOCTYPE html>
<html lang="en">
<head>
<meta charset="utf-8">
<title>Rising Paths Coaching</title>
<link href="https://fonts.googleapis.com/css2?family=Cinzel:wght@400;600;700&family=Montserrat:wght@400;500&family=Playfair+Display:wght@400;700&display=swap" rel="stylesheet">
<style>
:root{
  --teal:#17aca0;
  --teal-dark:#0f958a;
  --teal-soft:#b4e4df;
  --ink:#1f2426;
  --body:#4a4f52;
  --grey:#efefef;
  --footer:#3d3e40;
  --white:#ffffff;
}
*{margin:0;padding:0;box-sizing:border-box}
html,body{width:1200px;height:4320px;overflow:hidden;background:var(--white)}
body{font-family:"Playfair Display",Georgia,serif;color:var(--body)}
.page{position:relative;width:1200px;height:4320px;overflow:hidden}
.abs{position:absolute}
.heading{font-family:"Cinzel",Georgia,serif;font-weight:600;color:var(--ink);letter-spacing:1px}
.btn{position:absolute;background:var(--teal);color:var(--white);font-family:"Cinzel",serif;font-weight:700;font-size:13px;border-radius:20px;display:flex;align-items:center;justify-content:center;letter-spacing:.5px}
.photo{position:absolute}

/* header */
.topbar{left:565px;top:0;width:635px;height:50px;background:var(--teal);border-radius:25px 0 0 25px;display:flex;align-items:center;color:var(--white);font-family:"Cinzel",serif;font-weight:700;font-size:15px}
.topbar .book{margin-left:30px;width:250px}
.topbar .call{display:flex;align-items:center;gap:8px}
.topbar .soc{display:flex;gap:8px;margin-left:24px}
.topbar .soc span{width:16px;height:16px;border-radius:50%;background:var(--white)}
.header{left:0;top:50px;width:1200px;height:80px;background:var(--white)}
.logo-badge{left:148px;top:14px;width:166px;height:166px;border-radius:50%;background:var(--white);border:2px solid var(--teal);z-index:3;display:flex;align-items:center;justify-content:center}
.logo-badge .name{font-family:"Cinzel",serif;font-weight:600;font-size:20px;color:var(--ink)}
.nav{left:400px;top:88px;display:flex;font-family:"Cinzel",serif;font-weight:600;font-size:13px;color:var(--ink)}
.nav a{text-decoration:none;color:inherit;margin-right:33px}
.nav a.active{color:var(--teal)}

/* hero */
.hero{left:0;top:130px;width:1200px;height:700px;background:linear-gradient(180deg,#6f9ea1 0%,#a9bdb9 40%,#d8b9a8 70%,#c7a79c 100%)}
.hero-title{left:0;top:250px;width:1200px;text-align:center;font-family:"Cinzel",serif;font-weight:400;font-size:86px;color:var(--white);letter-spacing:2px}
.hero-sub{left:0;top:365px;width:1200px;text-align:center;font-family:"Montserrat",sans-serif;font-size:40px;letter-spacing:14px;color:var(--white)}

/* about */
.about-photo{left:110px;top:950px;width:446px;height:446px;border-radius:50%;background:linear-gradient(160deg,#c7c1ba,#e9e6e1 60%,#bfb5a8);border:3px solid var(--white);box-shadow:0 0 0 3px var(--teal)}
.about-title{left:620px;top:980px;font-size:48px}
.about-text{left:620px;top:1055px;width:400px;font-size:12.5px;line-height:21.2px;color:var(--body)}

/* services */
.services-title{left:0;top:1620px;width:1200px;text-align:center;font-size:40px}
.services-intro{left:290px;top:1688px;width:620px;text-align:center;font-size:13px;line-height:21px}
.svc{position:absolute;top:1765px;width:300px;text-align:center}
.svc .pic{width:240px;height:240px;border-radius:50%;margin:0 auto;border:4px solid var(--white);box-shadow:0 0 0 2px var(--teal)}
.svc h3{margin-top:20px;font-size:15px;font-weight:700;color:var(--ink);letter-spacing:.5px}
.svc p{margin-top:10px;font-size:12.5px;line-height:21px}

/* testimonials */
.testi-title{left:0;top:2500px;width:1200px;text-align:center;font-size:46px}
.quote-mark{font-family:"Playfair Display",serif;font-weight:700;font-size:90px;color:var(--teal);line-height:1}
.testi-text{left:200px;top:2597px;width:800px;text-align:center;font-size:19px;line-height:32px;color:#3a3f42}
.testi-name{left:0;top:2768px;width:1200px;text-align:center;font-family:"Cinzel",serif;font-weight:700;font-size:17px;color:var(--teal)}
.dots{left:536px;top:2844px;display:flex;gap:14px}
.dots span{width:14px;height:14px;border-radius:50%;background:#d6d6d6}
.dots span.on{background:#4a4a4a}

/* follow */
.follow-title{left:0;top:3090px;width:1200px;text-align:center;font-size:46px}
.tile{position:absolute;top:3200px;width:227px;height:245px;border-radius:10px}

/* newsletter */
.news-title{left:0;top:3690px;width:1200px;text-align:center;font-size:28px;color:var(--white)}
.news-text{left:0;top:3738px;width:1200px;text-align:center;font-size:14px;color:var(--white)}
.news-input{left:345px;top:3778px;width:355px;height:35px;background:var(--white);border-radius:18px;font-size:11px;color:#444;padding-left:12px;display:flex;align-items:center}
.news-btn{left:705px;top:3778px;width:128px;height:35px;background:var(--footer);color:var(--white);border-radius:18px;font-family:"Cinzel",serif;font-weight:700;font-size:12px;display:flex;align-items:center;justify-content:center}

/* footer */
.footer{left:0;top:3845px;width:1200px;height:475px;background:var(--footer)}
.f-head{position:absolute;top:3954px;font-family:"Cinzel",serif;font-weight:600;font-size:20px;color:var(--teal)}
.f-list{position:absolute;top:4006px;font-size:12.5px;line-height:24px;color:#e5e5e5}
.f-contact{position:absolute;display:flex;gap:14px;font-size:13px;line-height:21px;color:#e5e5e5}
.f-icon{width:40px;height:40px;border-radius:50%;background:var(--teal);flex:none;display:flex;align-items:center;justify-content:center}
.f-logo{left:532px;top:3960px;width:200px;height:140px;display:flex;align-items:center;justify-content:center;border-radius:50%;font-family:"Cinzel",serif;font-weight:600;font-size:22px;color:var(--white)}
.f-social{left:560px;top:4162px;display:flex;gap:12px}
.f-social span{width:34px;height:34px;border-radius:50%;background:#d0d0d0}
.copyright{left:0;top:4262px;width:1200px;text-align:center;font-size:13px;color:#e5e5e5}
</style>
</head>
<body>
<div class="page">

  <!-- hero -->
  <div class="abs hero" role="img" aria-label="Photo of a woman leaping at sunset with birds flying over misty hills"></div>
  <svg class="abs" style="left:0;top:520px" width="1200" height="330" viewBox="0 0 1200 330">
    <path d="M0 0 C250 230 900 260 1200 40 L1200 330 L0 330 Z" fill="#ffffff"/>
    <path d="M0 20 C260 250 880 270 1200 60" fill="none" stroke="var(--teal)" stroke-width="10"/>
    <path d="M0 60 C280 280 900 290 1200 90" fill="none" stroke="var(--teal)" stroke-width="4"/>
  </svg>
  <div class="abs hero-title">RISING PATHS</div>
  <div class="abs hero-sub">COACHING</div>

  <!-- header -->
  <div class="abs header"></div>
  <div class="abs topbar">
    <span class="book">BOOK AN APPOINTMENT</span>
    <span class="call">
      <svg width="14" height="14" viewBox="0 0 24 24"><path fill="#fff" d="M6.6 10.8a15 15 0 0 0 6.6 6.6l2.2-2.2c.3-.3.7-.4 1-.2 1.1.4 2.3.6 3.6.6.6 0 1 .4 1 1V20c0 .6-.4 1-1 1A17 17 0 0 1 3 4c0-.6.4-1 1-1h3.5c.6 0 1 .4 1 1 0 1.3.2 2.5.6 3.6.1.3 0 .7-.2 1z"/></svg>
      CALL: 55501234
    </span>
    <span class="soc"><span></span><span></span></span>
  </div>
  <div class="abs logo-badge"><span class="name">Rising Paths</span></div>
  <nav class="abs nav">
    <a class="active" href="#">HOME</a>
    <a href="#">ABOUT MY SERVICES</a>
    <a href="#">ABOUT ME</a>
    <a href="#">SCHEDULING</a>
    <a href="#">TESTIMONIALS</a>
    <a href="#">BLOG</a>
  </nav>

  <!-- about me -->
  <div class="photo about-photo" role="img" aria-label="Portrait of the coach smiling at a desk with a notebook"></div>
  <h2 class="abs heading about-title">ABOUT ME</h2>
  <p class="abs about-text">Lorem ipsum dolor sit amet, consectetur adipiscing elit, sed do eiusmod tempor incididunt ut labore et dolore magna aliqua.uis ipsum suspendisse ultrices gravida. Risus commodo viverlorera maecenas accumsan lacus vel facilisis. Lorem ipsum dolor sit amet, consectetur adipiscing elit, sed do eiusmod tempor incididunt ut labore et dolore magna aliqua. Quis ipsum suspendisse ultrices gravida. Risus commodo viverra maecenas accumsan lacus vel facilisis. Lorem ipsum dolor sit amet, consectetur adipiscing elit, sed do eiusmod tempor incididunt ut labore et dolore magna alua. Quis ipsum suspendisse ultrices gravida. Risus commodo viverra maecenas accumsan lacus vel facilisis.</p>
  <div class="btn" style="left:620px;top:1302px;width:120px;height:38px">READ MORE</div>

  <!-- services -->
  <svg class="abs" style="left:0;top:1515px" width="1200" height="830" viewBox="0 0 1200 830">
    <path d="M0 70 C300 -10 900 -10 1200 70 L1200 745 C900 830 300 830 0 745 Z" fill="var(--teal-soft)"/>
    <path d="M0 62 C300 -18 900 -18 1200 62" fill="none" stroke="var(--teal)" stroke-width="4"/>
    <path d="M0 752 C300 838 900 838 1200 752" fill="none" stroke="var(--teal)" stroke-width="5"/>
  </svg>
  <h2 class="abs heading services-title">ABOUT MY SERVICES</h2>
  <p class="abs services-intro">Lorem ipsum dolor sit amet, consectetur adipiscing elit, sed do eiusmod tempor incididunt ut labore et dolore magna aliqua.uis ipsum suspendisse ultrices gravida. Risus commodo viverlorera maece</p>
  <div class="svc" style="left:123px">
    <div class="pic" role="img" aria-label="Photo of two women talking on a sofa" style="background:linear-gradient(150deg,#5d5c5f,#c9b8a6)"></div>
    <h3>ONE TO ONE COACHING</h3>
    <p>Lorem ipsum dolor sit amet, consectetur adipiscing elit, sed do eiusmod tempor incididunt ut labore et dolore</p>
  </div>
  <div class="svc" style="left:448px">
    <div class="pic" role="img" aria-label="Photo of a group seated in a bright room facing a speaker" style="background:linear-gradient(150deg,#e8e3dc,#a58a76)"></div>
    <h3>GROUP COACHING</h3>
    <p>Lorem ipsum dolor sit amet, consectetur adipiscing elit, sed do eiusmod tempor incididunt ut labore et dolore</p>
  </div>
  <div class="svc" style="left:770px">
    <div class="pic" role="img" aria-label="Photo of a woman leading a meeting by a window" style="background:linear-gradient(150deg,#d7dde0,#4b4f55)"></div>
    <h3>LEADERSHIP COACHING</h3>
    <p>Lorem ipsum dolor sit amet, consectetur adipiscing elit, sed do eiusmod tempor incididunt ut labore et dolore</p>
  </div>
  <div class="btn" style="left:540px;top:2203px;width:132px;height:38px">READ MORE</div>

  <!-- testimonials -->
  <svg class="abs" style="left:0;top:2290px" width="1200" height="700" viewBox="0 0 1200 700">
    <path d="M0 50 C300 135 900 135 1200 50 L1200 400 C1000 680 200 680 0 400 Z" fill="var(--grey)"/>
    <path d="M0 400 C200 680 1000 680 1200 400" fill="none" stroke="var(--teal)" stroke-width="8"/>
    <path d="M0 440 C200 715 1000 715 1200 440" fill="none" stroke="var(--teal)" stroke-width="3"/>
  </svg>
  <h2 class="abs heading testi-title">TESTIMONIALS</h2>
  <div class="abs quote-mark" style="left:205px;top:2540px">&ldquo;</div>
  <p class="abs testi-text">Lorem ipsum dolor sit amet, consectetur adipiscing elit, sed do eiusmod tempor incidid labore et dolore magna aliqua. Quis ipsum suspendisse ultrices gravida. Risus commodo viverra maecenas accumsan lacus veetur adipiscing elit, sed do eiusmod tempor incididunt ut labore et dolore magna aliqua. Quis ipsum suspendisse ultrices gravida. Rl facilisis.</p>
  <div class="abs quote-mark" style="left:935px;top:2703px">&rdquo;</div>
  <div class="abs testi-name">MARLA QUINNET</div>
  <div class="abs dots"><span class="on"></span><span></span><span></span><span></span><span></span></div>

  <!-- follow us -->
  <h2 class="abs heading follow-title">FOLLOW US</h2>
  <div class="tile" style="left:105px;background:linear-gradient(180deg,#8fb3cf,#6d8a94 60%,#3f6f86)" role="img" aria-label="Photo of a wooden signpost beside a lake and mountains"></div>
  <div class="tile" style="left:360px;background:linear-gradient(150deg,#e6e2dc,#8a7a6a)" role="img" aria-label="Photo of two women working together at a desk"></div>
  <div class="tile" style="left:613px;background:linear-gradient(180deg,#2b8fc4,#1f6f9e)" role="img" aria-label="Photo of a wooden figure climbing wooden steps on blue"></div>
  <div class="tile" style="left:868px;background:linear-gradient(180deg,#a7b6c0,#596670 70%,#2f2f30)" role="img" aria-label="Photo of a person with raised arms on a mountain top"></div>

  <!-- newsletter -->
  <svg class="abs" style="left:0;top:3585px" width="1200" height="290" viewBox="0 0 1200 290">
    <path d="M0 40 C300 -5 900 -5 1200 40 L1200 290 L0 290 Z" fill="var(--teal)"/>
    <path d="M0 22 C300 -22 900 -22 1200 22" fill="none" stroke="var(--teal)" stroke-width="4"/>
  </svg>
  <h2 class="abs heading news-title">SIGN UP NEWSLETTER</h2>
  <p class="abs news-text">Lorem ipsum dolor sit amet, consectetur adipiscing elit, sed do eiusmod tempor</p>
  <div class="abs news-input">Email:</div>
  <div class="abs news-btn">SIGN ME UP!</div>

  <!-- footer -->
  <div class="abs footer"></div>
  <div class="f-head" style="left:137px">CONTACT US</div>
  <div class="f-contact" style="left:128px;top:3995px">
    <span class="f-icon"><svg width="16" height="16" viewBox="0 0 24 24"><path fill="#fff" d="M12 2a7 7 0 0 0-7 7c0 5 7 13 7 13s7-8 7-13a7 7 0 0 0-7-7zm0 9.5A2.5 2.5 0 1 1 12 6.5a2.5 2.5 0 0 1 0 5z"/></svg></span>
    <span>Location Name<br>14 Willow Court<br>Brookfield 3318</span>
  </div>
  <div class="f-contact" style="left:128px;top:4080px;align-items:center">
    <span class="f-icon"><svg width="16" height="16" viewBox="0 0 24 24"><path fill="none" stroke="#fff" stroke-width="2" d="M3 5h18v14H3zM3 6l9 6 9-6"/></svg></span>
    <span>hello@risingpaths.example</span>
  </div>
  <div class="f-head" style="left:382px">LINKS</div>
  <div class="f-list" style="left:382px">Home<br>Coaching<br>About me<br>My background<br>Scheduling<br>Testimonials<br>Blogs</div>
  <div class="abs f-logo">Rising Paths</div>
  <div class="f-head" style="left:785px">SUPPORT</div>
  <div class="f-list" style="left:785px">Lorem ipsum<br>dolor sit amet,<br>consectetur<br>adipiscing elit,<br>sed dousmod<br>tempor</div>
  <div class="f-head" style="left:943px">HELP</div>
  <div class="f-list" style="left:943px">Lorem ipsum<br>dolor sit amet<br>Consectetur adip<br>Rcing elit<br>Ed dousmod<br>Wmpor incididun<br>Qabore et dous</div>
  <div class="abs f-social"><span></span><span></span><span></span></div>
  <div class="abs copyright">© 2022 All Rights Reserved.Terms &amp; Conditions Privacy Policy</div>

</div>
</body>
</html>
```